IT services company requires Letterhead design

We need a professional letterhead designed to be used for general correspondence with customers, quotes, invoices etc. We are a new IT services company specialising in computer servicing and repairs and mobile and tablet repairs. Attached are templates that my printing company have supplied, my logos, an interpretation of our website for you to get a feel of the company. Details to be included on the letterhead are

Company Number – 4738261
VAT Number - 518337942
Registered Address – 14-16 Brambly Lane, London, E4 9QT

Phone – 01632 487215
Email – sales@quorvent.com
Web – www.quorvent.com

I would prefer for the top of the letterhead to just have the company logo on a white background and the rest of the details on the bottom of the letterhead but I am open to design ideas.

Thanks

```html
<!DOCTYPE html>
<html lang="en">
<head>
<meta charset="utf-8">
<title>Quorvent Letterhead – Colour Variants</title>
<link rel="stylesheet" href="https://fonts.googleapis.com/css2?family=Exo+2:wght@700&family=Catamaran:wght@400;500&display=swap">
<style>
  :root {
    --cyan: #35c2e6;
    --ink: #0f1720;
    --ink-soft: #2b2f33;
    --paper: #ffffff;
    --mist: #e6f2f6;
    --mist-deep: #d6ebf2;
    --footer-text-light: #ffffff;
    --footer-text-dark: #3a3f44;
    --shadow: rgba(0, 0, 0, 0.45);
  }
  * { box-sizing: border-box; margin: 0; padding: 0; }
  html, body { width: 1200px; height: 633px; overflow: hidden; background: var(--paper); }
  .presentation { position: relative; width: 1200px; height: 633px; }

  .sheet {
    position: absolute; top: 59px; width: 353px; height: 495px;
    background: var(--paper);
    box-shadow: 8px 10px 12px var(--shadow);
  }
  .sheet--cyan { left: 36px; }
  .sheet--light { left: 422px; }
  .sheet--dark { left: 808px; }

  .sheet__header { position: absolute; top: 0; left: 0; right: 0; height: 54px; }
  .sheet--cyan .sheet__header { background: var(--cyan); }
  .sheet--light .sheet__header { background: linear-gradient(90deg, var(--paper) 0%, var(--paper) 45%, var(--mist) 100%); }
  .sheet--dark .sheet__header { background: var(--ink); }

  .brand {
    position: absolute; left: 16px; top: 13px;
    display: flex; align-items: center; gap: 6px;
    font-family: "Exo 2", sans-serif; font-weight: 700; font-size: 26px; line-height: 1;
    letter-spacing: -0.3px;
  }
  .brand__dot { width: 6px; height: 6px; }
  .sheet--cyan .brand { color: var(--paper); }
  .sheet--cyan .brand__dot { background: var(--paper); }
  .sheet--light .brand { color: var(--ink-soft); }
  .sheet--light .brand__dot { background: var(--cyan); }
  .sheet--dark .brand { color: var(--paper); }
  .sheet--dark .brand__dot { background: var(--cyan); }

  .sheet__footer {
    position: absolute; left: 0; right: 0; bottom: 0; height: 53px;
    font-family: "Catamaran", sans-serif; font-weight: 500; font-size: 7.3px; line-height: 1;
  }
  .sheet--cyan .sheet__footer { background: var(--cyan); color: var(--footer-text-light); }
  .sheet--light .sheet__footer { background: linear-gradient(90deg, var(--mist) 0%, var(--paper) 100%); color: var(--footer-text-dark); }
  .sheet--dark .sheet__footer { background: var(--ink); color: var(--footer-text-light); }

  .legal { position: absolute; left: 66px; top: 9px; }
  .legal p { white-space: nowrap; height: 10.3px; }
  .legal__mark { position: absolute; left: -18px; top: 1px; width: 8px; height: 8px; }
  .legal__pin { position: absolute; left: -17px; top: 30px; width: 8px; height: 10px; }
  .sheet--cyan .legal__mark { background: var(--paper); }
  .sheet--light .legal__mark, .sheet--dark .legal__mark { background: var(--cyan); }

  .contact { position: absolute; left: 234px; top: 8px; list-style: none; }
  .contact li { display: flex; align-items: center; gap: 5px; height: 14.5px; white-space: nowrap; }
  .contact svg { width: 9px; height: 9px; flex: none; }

  .icon { fill: currentColor; }
  .sheet--light .icon, .sheet--dark .icon--accent { fill: var(--cyan); }
  .sheet--dark .icon { fill: var(--paper); }
  .sheet--dark .icon--accent { fill: var(--paper); }
  .sheet--cyan .icon { fill: var(--paper); }
</style>
</head>
<body>
<main class="presentation">

  <section class="sheet sheet--cyan" aria-label="Letterhead, cyan variant">
    <header class="sheet__header">
      <div class="brand"><span class="brand__dot"></span>Quorvent</div>
    </header>
    <footer class="sheet__footer">
      <div class="legal">
        <span class="legal__mark"></span>
        <svg class="legal__pin icon" viewBox="0 0 8 10"><path d="M4 0a4 4 0 0 1 4 4c0 3-4 6-4 6S0 7 0 4a4 4 0 0 1 4-4zm0 2.3a1.7 1.7 0 1 0 0 3.4 1.7 1.7 0 0 0 0-3.4z"/></svg>
        <p>Company Number – 4738261</p>
        <p>VAT Number - 518337942</p>
        <p>Registered Address - 14-16</p>
        <p>Brambly Lane, London, E4 9QT</p>
      </div>
      <ul class="contact">
        <li><svg class="icon" viewBox="0 0 10 10"><path d="M2 0h2l1 2.5-1.3 1a5 5 0 0 0 2.8 2.8l1-1.3L10 6v2a2 2 0 0 1-2 2A8 8 0 0 1 0 2a2 2 0 0 1 2-2z"/></svg>01632 487215</li>
        <li><svg class="icon" viewBox="0 0 10 10"><path d="M0 3l5 3 5-3v6H0z M1 1h8l-4 3z"/></svg>sales@quorvent.com</li>
        <li><svg class="icon" viewBox="0 0 10 10"><rect x="0" y="1.5" width="10" height="7"/></svg>quorvent.com</li>
      </ul>
    </footer>
  </section>

  <section class="sheet sheet--light" aria-label="Letterhead, light variant">
    <header class="sheet__header">
      <div class="brand"><span class="brand__dot"></span>Quorvent</div>
    </header>
    <footer class="sheet__footer">
      <div class="legal">
        <span class="legal__mark"></span>
        <svg class="legal__pin icon" viewBox="0 0 8 10"><path d="M4 0a4 4 0 0 1 4 4c0 3-4 6-4 6S0 7 0 4a4 4 0 0 1 4-4zm0 2.3a1.7 1.7 0 1 0 0 3.4 1.7 1.7 0 0 0 0-3.4z"/></svg>
        <p>Company Number – 4738261</p>
        <p>VAT Number - 518337942</p>
        <p>Registered Address - 14-16</p>
        <p>Brambly Lane, London, E4 9QT</p>
      </div>
      <ul class="contact">
        <li><svg class="icon" viewBox="0 0 10 10"><path d="M2 0h2l1 2.5-1.3 1a5 5 0 0 0 2.8 2.8l1-1.3L10 6v2a2 2 0 0 1-2 2A8 8 0 0 1 0 2a2 2 0 0 1 2-2z"/></svg>01632 487215</li>
        <li><svg class="icon" viewBox="0 0 10 10"><path d="M0 3l5 3 5-3v6H0z M1 1h8l-4 3z"/></svg>sales@quorvent.com</li>
        <li><svg class="icon" viewBox="0 0 10 10"><rect x="0" y="1.5" width="10" height="7"/></svg>quorvent.com</li>
      </ul>
    </footer>
  </section>

  <section class="sheet sheet--dark" aria-label="Letterhead, dark variant">
    <header class="sheet__header">
      <div class="brand"><span class="brand__dot"></span>Quorvent</div>
    </header>
    <footer class="sheet__footer">
      <div class="legal">
        <span class="legal__mark"></span>
        <svg class="legal__pin icon" viewBox="0 0 8 10"><path d="M4 0a4 4 0 0 1 4 4c0 3-4 6-4 6S0 7 0 4a4 4 0 0 1 4-4zm0 2.3a1.7 1.7 0 1 0 0 3.4 1.7 1.7 0 0 0 0-3.4z"/></svg>
        <p>Company Number – 4738261</p>
        <p>VAT Number - 518337942</p>
        <p>Registered Address - 14-16</p>
        <p>Brambly Lane, London, E4 9QT</p>
      </div>
      <ul class="contact">
        <li><svg class="icon" viewBox="0 0 10 10"><path d="M2 0h2l1 2.5-1.3 1a5 5 0 0 0 2.8 2.8l1-1.3L10 6v2a2 2 0 0 1-2 2A8 8 0 0 1 0 2a2 2 0 0 1 2-2z"/></svg>01632 487215</li>
        <li><svg class="icon" viewBox="0 0 10 10"><path d="M0 3l5 3 5-3v6H0z M1 1h8l-4 3z"/></svg>sales@quorvent.com</li>
        <li><svg class="icon" viewBox="0 0 10 10"><rect x="0" y="1.5" width="10" height="7"/></svg>quorvent.com</li>
      </ul>
    </footer>
  </section>

</main>
</body>
</html>
```